New Fun, Positive, energised looking Business Card Needed for High Achiever Coach

I am looking for a two sided full colour business card. I am self employed and have recently re branded my 1-2-1 work re-vitalising high achievers. My target client base for these cards is therefore high achievers - usually aged 40 -55, they are often entrepreneurs, CEO or work in banking and finance and 2/3 are male. I work with them on 90 day or 6 month coaching programs to help them live their success in a healthier, more sustainable and fulfiiled way. They pay for this privately so though they are corporate types the cards need not look 'corporate'. I want to portray the idea of transformation, vitality and re-connecting.
You can get a feel for the look I like on my new website: morvenlakey.co.uk
I want to use this logo with strapline (Re-Vitalising High Achievers) (I purchased off Markfolio) and font/ colours (the turquoise and green).
Details to include on the card:
www.morvenlakey.co.uk
+44 7913 264518
morven@morvenlakey.co.uk
skype: morvenlakey
I'd also like to include:
Do you struggle to switch off? Want to be healthier and feel fitter? Want closer relationships? More clarity over the direction you are headed? I can help you do these things using integrated mind-body techniques. Visit morvenlakey.co.uk TODAY to apply for a FREE Breakthrough session.
BUT if that is too much text for a card I am open to advice/ammendments.
Updates
Thanks for your design - I am considering them. PLease change the wording to :

```html
<!DOCTYPE html>
<html lang="en">
<head>
<meta charset="utf-8">
<title>Morven Lakey – Business Card Options</title>
<link rel="stylesheet" href="https://fonts.googleapis.com/css2?family=Source+Sans+3:wght@400;600;700&display=swap">
<style>
  :root {
    --backdrop: #5a3322;
    --turquoise: #0aa5c8;
    --green: #5fbe6e;
    --paper: #ffffff;
    --ink: #2e2e2e;
    --label: #ffffff;
  }
  * { margin: 0; padding: 0; box-sizing: border-box; }
  html, body { width: 1200px; height: 715px; overflow: hidden; }
  body {
    position: relative;
    background: var(--backdrop);
    font-family: "Source Sans 3", "Helvetica Neue", Arial, sans-serif;
  }
  .card {
    position: absolute;
    width: 478px;
    height: 273px;
    overflow: hidden;
  }
  .card--front { left: 287px; top: 66px; background: var(--paper); }
  .card--back-white { left: 89px; top: 372px; background: var(--paper); color: var(--ink); }
  .card--back-green { left: 616px; top: 363px; background: var(--green); color: var(--paper); }

  .card__bands { position: absolute; inset: 0; }

  .brand { position: absolute; left: 26px; top: 121px; }
  .brand__name {
    font-weight: 700;
    font-size: 26px;
    line-height: 1;
    color: var(--turquoise);
  }
  .brand__strapline {
    margin-top: 6px;
    font-size: 12px;
    color: var(--turquoise);
  }

  .contact {
    position: absolute;
    right: 22px;
    top: 170px;
    list-style: none;
    text-align: right;
    color: var(--paper);
    font-size: 14px;
    line-height: 22.8px;
  }
  .contact__item { display: flex; justify-content: flex-end; align-items: center; gap: 5px; }
  .contact__icon { width: 11px; height: 11px; flex: none; }

  .pitch {
    position: absolute;
    inset: 0;
    padding-top: 42px;
    text-align: center;
    font-size: 17px;
    line-height: 21px;
  }
  .pitch__questions { margin-bottom: 9px; }
  .pitch__offer { margin-bottom: 6px; line-height: 18.5px; }
  .pitch__cta { line-height: 18.5px; }
  .pitch__cta strong { font-weight: 700; }

  .option-label {
    position: absolute;
    top: 653px;
    font-size: 27px;
    color: var(--label);
    transform: translateX(-50%);
  }
  .option-label--two { left: 326px; }
  .option-label--one { left: 871px; }
</style>
</head>
<body>

<section class="card card--front" aria-label="Card front">
  <svg class="card__bands" viewBox="0 0 478 273" aria-hidden="true">
    <polygon fill="var(--green)" points="0,226 478,106 478,116 0,236"/>
    <polygon fill="var(--turquoise)" points="0,241 478,121 478,273 0,273"/>
  </svg>

  <div class="brand">
    <p class="brand__name">Morven Lakey</p>
    <p class="brand__strapline">Re-Vitalising High Achievers</p>
  </div>

  <ul class="contact">
    <li class="contact__item">
      <svg class="contact__icon" viewBox="0 0 12 12" aria-hidden="true"><circle cx="6" cy="6" r="5.2" fill="none" stroke="#fff" stroke-width="1"/><path d="M4.2 3.2 L5.2 4.6 L4.6 5.3 C5 6.2 5.8 7 6.7 7.4 L7.4 6.8 L8.8 7.8 L8.2 8.8 C6 8.6 3.4 6 3.2 3.8 Z" fill="#fff"/></svg>
      <span>+44 7913 264518</span>
    </li>
    <li class="contact__item">
      <svg class="contact__icon" viewBox="0 0 12 12" aria-hidden="true"><rect x="1" y="3" width="10" height="7" fill="#fff"/><path d="M1 3 L6 7 L11 3" fill="none" stroke="var(--turquoise)" stroke-width="1"/></svg>
      <span>morven@morvenlakey.co.uk</span>
    </li>
    <li class="contact__item">
      <svg class="contact__icon" viewBox="0 0 12 12" aria-hidden="true"><g fill="none" stroke="#fff" stroke-width="1"><circle cx="6" cy="6" r="5"/><ellipse cx="6" cy="6" rx="2.2" ry="5"/><path d="M1 6 H11 M2 3.5 H10 M2 8.5 H10"/></g></svg>
      <span>www.morvenlakey.co.uk</span>
    </li>
    <li class="contact__item">
      <svg class="contact__icon" viewBox="0 0 12 12" aria-hidden="true"><circle cx="6" cy="6" r="5" fill="none" stroke="#fff" stroke-width="1.2"/></svg>
      <span>morvenlakey</span>
    </li>
  </ul>
</section>

<section class="card card--back-white" aria-label="Card back, white option">
  <div class="pitch">
    <p class="pitch__questions">Do you struggle to switch off?<br>Want to be healthier and feel fitter?<br>Want closer relationships?<br>More clarity over the direction you are headed?</p>
    <p class="pitch__offer">Let me help you reach your goals using integrated<br>mind-body techniques.</p>
    <p class="pitch__cta">Visit <strong>morvenlakey.co.uk</strong> TODAY to apply for a<br>FREE Breakthrough session.</p>
  </div>
</section>

<section class="card card--back-green" aria-label="Card back, green option">
  <div class="pitch">
    <p class="pitch__questions">Do you struggle to switch off?<br>Want to be healthier and feel fitter?<br>Want closer relationships?<br>More clarity over the direction you are headed?</p>
    <p class="pitch__offer">Let me help you reach your goals using integrated<br>mind-body techniques.</p>
    <p class="pitch__cta">Visit <strong>morvenlakey.co.uk</strong> TODAY to apply for a<br>FREE Breakthrough session.</p>
  </div>
</section>

<p class="option-label option-label--two">Option # 2</p>
<p class="option-label option-label--one">Option # 1</p>

</body>
</html>
```